Brell Harbor Company Business Cards

Front and Back Business Card - logo and text setup - cool design. I need workable photoshop or illustrator files so I can setup each employee card with design that is created
Updates

Hi everyone, thank you for the great entries. Please no more white and blue cards - there are so many already - black and silver only now please. thanks!

Target Market(s)

Construction Industry - Facility Managers

Industry/Entity Type

Construction

Contact Information for Business Card

I really like contemporary simplistic looks - clean neat....not opposed to seeing some black backrounds

Requirements
Must have
• Logo/website address with design on front only - www.brellharbor-example.com (logo attached)
• Back:
• Name/Title/Company Address/Phone/email address
Nice to have
• Cool design
Should not have
• Nothing gimmicky like Fire or Water - since we are a Fire Protection company - it has all been done

```html
<!DOCTYPE html>
<html lang="en">
<head>
<meta charset="utf-8">
<title>Brell Harbor Company – Business Cards</title>
<link rel="stylesheet" href="https://fonts.googleapis.com/css2?family=Source+Sans+3:wght@400;700&display=swap">
<style>
  :root {
    --navy: #22447a;
    --signal: #ef4a36;
    --graphite-light: #7b7c81;
    --graphite-dark: #2a2829;
    --paper: #ececec;
    --white: #ffffff;
  }
  * { margin: 0; padding: 0; box-sizing: border-box; }
  html, body { width: 1200px; height: 1200px; overflow: hidden; }
  body {
    background: var(--paper);
    font-family: "Source Sans 3", "Myriad Pro", Arial, sans-serif;
    position: relative;
  }
  .wordmark {
    display: flex; align-items: center; gap: 10px;
    color: var(--navy); font-weight: 700; white-space: nowrap; line-height: 1;
  }
  .wordmark .mark-square { background: var(--signal); flex: none; }
  .brand-header { position: absolute; left: 72px; top: 80px; font-size: 62px; }
  .brand-header .mark-square { width: 30px; height: 30px; }

  .card { position: absolute; left: 408px; width: 696px; height: 384px; overflow: hidden; background: var(--white); }
  .card-front { top: 306px; }
  .card-back { top: 742px; }
  .card-bg { position: absolute; inset: 0; width: 100%; height: 100%; }

  .front-logo { position: absolute; left: 402px; top: 60px; font-size: 44px; }
  .front-logo .mark-square { width: 22px; height: 22px; }
  .holder-name { position: absolute; left: 33px; top: 62px; color: var(--white); font-weight: 700; font-size: 33px; }
  .holder-title { position: absolute; left: 33px; top: 108px; color: var(--white); font-weight: 400; font-size: 25px; }
  .contact-line {
    position: absolute; left: 32px;
    display: flex; align-items: center; gap: 22px;
    color: var(--white); font-weight: 700; font-size: 20px; line-height: 1.3;
    white-space: nowrap;
  }
  .contact-icon { display: block; width: 28px; height: 28px; flex: none; }
  .contact-address { top: 198px; }
  .contact-address .contact-icon { align-self: flex-start; margin-top: 2px; }
  .contact-email { top: 263px; }
  .contact-phone { top: 320px; }
  .contact-fax { position: absolute; left: 350px; top: 320px; line-height: 28px; color: var(--white); font-weight: 700; font-size: 20px; white-space: nowrap; }

  .back-logo { position: absolute; left: 0; right: 0; top: 140px; justify-content: center; font-size: 54px; }
  .back-logo .mark-square { width: 26px; height: 26px; }
  .back-url { position: absolute; left: 0; right: 0; top: 234px; text-align: center; color: var(--signal); font-weight: 700; font-size: 28px; white-space: nowrap; }
</style>
</head>
<body>

<div class="wordmark brand-header"><span class="mark-square"></span>Brell Harbor</div>

<section class="card card-front" aria-label="Business card, contact side">
  <svg class="card-bg" viewBox="0 0 870 480" preserveAspectRatio="none" aria-hidden="true">
    <defs>
      <linearGradient id="graphite-front" x1="0" y1="0" x2="1" y2="0">
        <stop offset="0" stop-color="var(--graphite-light)"/>
        <stop offset="1" stop-color="var(--graphite-dark)"/>
      </linearGradient>
    </defs>
    <path fill="url(#graphite-front)" d="M0 0 L180 0 L305 24 C322 28 331 40 330 57 L325 132 C325 145 345 155 360 152 L450 147 C466 146 476 160 475 177 L465 327 C478 342 497 343 510 330 L580 257 C592 246 610 245 620 267 L660 352 C670 365 690 366 700 357 L790 272 C805 260 826 266 830 282 L870 412 L870 480 L0 480 Z"/>
    <rect x="0" y="0" width="24" height="480" fill="var(--navy)"/>
  </svg>

  <div class="wordmark front-logo"><span class="mark-square"></span>Brell Harbor</div>

  <div class="holder-name">Mr. RT</div>
  <div class="holder-title">Owner</div>

  <div class="contact-line contact-address">
    <svg class="contact-icon" viewBox="0 0 28 28" aria-hidden="true"><circle cx="14" cy="14" r="14" fill="var(--white)"/><path d="M14 6.5c-3 0-5.2 2.3-5.2 5.1 0 3.6 5.2 9.4 5.2 9.4s5.2-5.8 5.2-9.4c0-2.8-2.2-5.1-5.2-5.1z" fill="var(--signal)"/><circle cx="14" cy="11.6" r="2" fill="var(--white)"/></svg>
    <span>48 Quarry Lane<br>Millbrook, NY 10990</span>
  </div>
  <div class="contact-line contact-email">
    <svg class="contact-icon" viewBox="0 0 28 28" aria-hidden="true"><circle cx="14" cy="14" r="14" fill="var(--white)"/><rect x="7" y="9" width="14" height="10" fill="none" stroke="var(--signal)" stroke-width="1.6"/><path d="M7 9l7 6 7-6M7 19l5-5M21 19l-5-5" fill="none" stroke="var(--signal)" stroke-width="1.4"/></svg>
    <span>info@brellharbor-example.com</span>
  </div>
  <div class="contact-line contact-phone">
    <svg class="contact-icon" viewBox="0 0 28 28" aria-hidden="true"><circle cx="14" cy="14" r="14" fill="var(--white)"/><path d="M9.5 7.5l2.6 -.4 1.3 3.2-1.6 1.3c.8 1.8 2.2 3.2 4 4l1.3-1.6 3.2 1.3-.4 2.6c-.2 1-1 1.6-2 1.5-5-.6-9-4.6-9.6-9.6-.1-1 .5-1.8 1.2-2.3z" fill="var(--signal)"/></svg>
    <span>T: (555) 014-2290</span>
  </div>
  <div class="contact-fax">F: (555) 014-2291</div>
</section>

<section class="card card-back" aria-label="Business card, logo side">
  <svg class="card-bg" viewBox="0 0 868 480" preserveAspectRatio="none" aria-hidden="true">
    <defs>
      <linearGradient id="graphite-back" x1="0" y1="0" x2="1" y2="0">
        <stop offset="0" stop-color="var(--graphite-light)"/>
        <stop offset="1" stop-color="var(--graphite-dark)"/>
      </linearGradient>
    </defs>
    <rect x="0" y="0" width="868" height="480" fill="url(#graphite-back)"/>
    <rect x="0" y="0" width="18" height="480" fill="var(--navy)"/>
    <rect x="851" y="0" width="17" height="480" fill="var(--signal)"/>
    <path fill="var(--white)" d="M210 62 L580 62 C680 62 735 150 728 210 L718 330 C712 375 670 405 620 406 L215 412 C165 412 135 375 138 330 L150 130 C153 90 175 62 210 62 Z"/>
  </svg>
  <div class="wordmark back-logo"><span class="mark-square"></span>Brell Harbor</div>
  <div class="back-url">www.brellharbor-example.com</div>
</section>

</body>
</html>
```